need a clean, modern job advertisement designed for social media (Facebook & Instagram).

The post is to advertise two positions:
• Leading Hand Boilermaker
• Dragline Fitter
We want the design to match our KRT Plant Services branding: blue, white, strong, professional, mining-industry style.
What the design should include:
Bold headline: “WE’RE HIRING”
Sub-headline: “Leading Hand Boilermaker & Dragline Fitter”
Key points:
• Bowen Basin based
• Dragline & shovel maintenance
• Great pay + long-term work
• Locally owned & operated
KRT logo placed cleanly
Space for 1–2 images (boilermaking or dragline work)
Design style:
Strong and industrial
Blue/white colour scheme
Easy to read at a glance
Suitable for a square 1080×1080 design

```html
<!DOCTYPE html>
<html lang="en">
<head>
<meta charset="utf-8">
<title>KRT Plant Services – We're Hiring</title>
<link href="https://fonts.googleapis.com/css2?family=Anton&family=Poppins:wght@400;500;700&display=swap" rel="stylesheet">
<style>
  :root{
    --brand-blue:#00b2f7;
    --ink:#000000;
    --paper:#ffffff;
    --bar-grey:#e7e7eb;
    --text-grey:#86868b;
    --navy:#0b2a4a;
    --photo-dark:#2a1d14;
    --photo-mid:#5a4330;
    --photo-warm:#8a6a44;
  }
  *{margin:0;padding:0;box-sizing:border-box}
  html,body{width:1200px;height:1200px;overflow:hidden;background:var(--paper)}
  .post{position:relative;width:1200px;height:1200px;background:var(--paper);overflow:hidden;font-family:"Poppins",sans-serif}
  .post-shapes{position:absolute;inset:0}
  .brand{position:absolute;left:71px;width:495px;top:150px;height:110px;display:flex;align-items:center;justify-content:center;gap:16px}
  .brand-mark{width:34px;height:34px;background:var(--brand-blue)}
  .brand-name{font-family:"Poppins",sans-serif;font-weight:700;font-size:40px;color:var(--navy);letter-spacing:.5px;white-space:nowrap}
  .headline-top{position:absolute;left:71px;width:495px;top:362px;text-align:center;font-family:"Anton",sans-serif;font-size:120px;line-height:1;color:var(--paper);letter-spacing:1px}
  .headline-box{position:absolute;left:71px;top:496px;width:495px;height:156px;background:var(--paper);display:flex;align-items:center;justify-content:center}
  .headline-main{font-family:"Anton",sans-serif;font-size:162px;line-height:1;color:var(--brand-blue);letter-spacing:1px;margin-top:4px}
  .subheadline{position:absolute;left:71px;width:495px;top:664px;text-align:center;font-weight:500;font-size:22px;color:var(--paper);white-space:nowrap}
  .perk{position:absolute;left:57px;height:60px;display:flex;align-items:center}
  .perk-label{position:absolute;left:85px;font-size:27px;font-weight:400;color:var(--text-grey);white-space:nowrap;line-height:60px}
  .perk-icon{position:absolute;left:0;top:0;width:69px;height:60px}
</style>
</head>
<body>
<main class="post">
  <svg class="post-shapes" width="1200" height="1200" viewBox="0 0 1200 1200" aria-hidden="false">
    <defs>
      <linearGradient id="photoTone" x1="0" y1="0" x2="1" y2="1">
        <stop offset="0" stop-color="var(--photo-warm)"/>
        <stop offset="0.5" stop-color="var(--photo-mid)"/>
        <stop offset="1" stop-color="var(--photo-dark)"/>
      </linearGradient>
    </defs>
    <!-- blue headline band -->
    <polygon class="headline-band" points="0,250 789,250 663,738 0,738" fill="var(--brand-blue)"/>
    <!-- perk bars -->
    <polygon class="perk-bar" points="100,804 643,804 678,864 100,864" fill="var(--bar-grey)"/>
    <polygon class="perk-bar" points="100,891 693,891 728,951 100,951" fill="var(--bar-grey)"/>
    <polygon class="perk-bar" points="100,978 743,978 778,1038 100,1038" fill="var(--bar-grey)"/>
    <polygon class="perk-bar" points="100,1064 793,1064 828,1124 100,1124" fill="var(--bar-grey)"/>
    <!-- black chevron stripe -->
    <polygon class="chevron-stripe" points="951,0 980,0 639,601 980,1200 951,1200 611,601" fill="var(--ink)"/>
    <!-- photo area -->
    <polygon class="photo-area" role="img" aria-label="Photo of a tradesman in hi-vis workwear and hard hat operating a magnetic drill under a crane hook in an industrial workshop" points="996,0 1200,0 1200,1200 1000,1200 663,601" fill="url(#photoTone)"/>
  </svg>

  <div class="brand">
    <span class="brand-mark"></span>
    <span class="brand-name">KRT Plant Services</span>
  </div>

  <h1 class="headline-top">WE’RE</h1>
  <div class="headline-box"><span class="headline-main">HIRING</span></div>
  <p class="subheadline">Leading Hand Boilermaker &amp; Dragline Fitter</p>

  <ul class="perks">
    <li class="perk" style="top:804px">
      <svg class="perk-icon" viewBox="0 0 69 60"><polygon points="17,0 52,0 69,30 52,60 17,60 0,30" fill="var(--brand-blue)"/>
        <g fill="none" stroke="#fff" stroke-width="2.2"><rect x="28" y="23" width="13" height="14"/><circle cx="24" cy="19" r="4.5"/><circle cx="45" cy="19" r="4.5"/><circle cx="24" cy="41" r="4.5"/><circle cx="45" cy="41" r="4.5"/></g></svg>
      <span class="perk-label">Bowen Basin based</span>
    </li>
    <li class="perk" style="top:891px">
      <svg class="perk-icon" viewBox="0 0 69 60"><polygon points="17,0 52,0 69,30 52,60 17,60 0,30" fill="var(--brand-blue)"/>
        <g fill="none" stroke="#fff" stroke-width="2.2"><circle cx="33" cy="28" r="9"/><circle cx="33" cy="28" r="4"/><path d="M33 15v-3M33 44v-3M20 28h-3M49 28h-3M24 19l-2-2M44 39l-2-2M24 37l-2 2M42 19l2-2"/><path d="M40 36l8 8"/></g></svg>
      <span class="perk-label">Dragline &amp; shovel maintenance</span>
    </li>
    <li class="perk" style="top:978px">
      <svg class="perk-icon" viewBox="0 0 69 60"><polygon points="17,0 52,0 69,30 52,60 17,60 0,30" fill="var(--brand-blue)"/>
        <g fill="none" stroke="#fff" stroke-width="2.2"><circle cx="36" cy="20" r="7"/><path d="M36 16v8M16 40l8-6h10l4 3h-9M38 37l10-6 3 3-12 10H24l-6 3"/></g></svg>
      <span class="perk-label">Great pay + long-term work</span>
    </li>
    <li class="perk" style="top:1064px">
      <svg class="perk-icon" viewBox="0 0 69 60"><polygon points="17,0 52,0 69,30 52,60 17,60 0,30" fill="var(--brand-blue)"/>
        <g fill="none" stroke="#fff" stroke-width="2.2"><circle cx="35" cy="17" r="5"/><path d="M32.5 17l2 2 3-4"/><path d="M16 30l7-5 8 3 5-3 7 2 9 4M22 33l9 9 3-2 3 2 3-3 3 1 3-4"/></g></svg>
      <span class="perk-label">Locally owned &amp; operated</span>
    </li>
  </ul>
</main>
</body>
</html>
```